Letterhead for a Natural Hair Run

We need a letterhead design with the logo uploaded entitled 'Zephlyra Dash'. This run is a natural 5K run seeking to promote the acceptance of natural beauty in every aspect of society encompassing one's ethnic roots and its connection to a healthy lifetstyle. We would like to see designs coordinating with our logo. The design should be fun and exciting!

Industry/Entity Type

Hair

Font styles to use
Serif
Sans Serif

Requirements
Must have
• Please included this information on the letter head:
• P.O. Box K7214
• Nassau, Bahamas
• Phone: (242) 618-2907
• Email: goskyward417@mailvista.net

```html
<!DOCTYPE html>
<html lang="en">
<head>
<meta charset="utf-8">
<title>Zephlyra Dash Letterhead</title>
<link href="https://fonts.googleapis.com/css2?family=PT+Serif&family=Questrial&display=swap" rel="stylesheet">
<style>
  :root {
    --backdrop: #ece8e2;
    --paper: #ffffff;
    --ink: #111111;
    --sky: #1aa6e0;
    --sun: #f5e11e;
  }
  * { margin: 0; padding: 0; box-sizing: border-box; }
  html, body {
    width: 1200px;
    height: 1000px;
    overflow: hidden;
    background: var(--backdrop);
  }
  .letterhead {
    position: absolute;
    left: 285px;
    top: 58px;
    width: 634px;
    height: 860px;
    background: var(--paper);
    box-shadow: 0 2px 10px rgba(0, 0, 0, 0.15);
  }
  .brand-name {
    position: absolute;
    left: 38px;
    top: 117px;
    font-family: "Questrial", sans-serif;
    font-size: 20px;
    letter-spacing: 1px;
    color: var(--ink);
    white-space: nowrap;
  }
  .contact {
    position: absolute;
    left: 427px;
    top: 58px;
    height: 64px;
    padding-left: 13px;
    padding-top: 5px;
    font-family: "PT Serif", serif;
    font-style: normal;
    font-size: 11px;
    line-height: 14px;
    color: var(--ink);
  }
  .contact::before,
  .contact::after {
    content: "";
    position: absolute;
    top: 0;
    width: 3px;
    height: 64px;
  }
  .contact::before { left: 0; background: var(--sky); }
  .contact::after { left: 4px; background: var(--sun); }
  .contact p { white-space: nowrap; }
  .header-rule {
    position: absolute;
    left: 258px;
    right: 0;
    height: 3px;
  }
  .header-rule--sky { top: 125px; background: var(--sky); }
  .header-rule--sun { top: 132px; background: var(--sun); }
  .footer-band {
    position: absolute;
    left: 0;
    right: 0;
    bottom: 0;
    height: 18px;
    background: linear-gradient(90deg, #fff200 0%, #c8dd6a 35%, #3fc1b8 70%, #00aeef 100%);
  }
</style>
</head>
<body>
  <main class="letterhead">
    <div class="brand-name">Zephlyra Dash</div>

    <address class="contact">
      <p>P.O. Box K7214</p>
      <p>Nassau, Bahamas</p>
      <p>Phone: (242) 618-2907</p>
      <p>Email: goskyward417@mailvista.net</p>
    </address>

    <div class="header-rule header-rule--sky"></div>
    <div class="header-rule header-rule--sun"></div>

    <div class="footer-band"></div>
  </main>
</body>
</html>
```